Standortübersicht - Deutschlandkarte
Hallo,
wir liefern Baustromverteiler deutschlandweit auf Baustellen.
www.kabelkastenleihe.de
Wir benötigen eine Grafik für unsere Homepage und für Flyer / Präsentationen
Die Grafik soll eine Deutschlandkarte zeigen mit unseren Standorten/Zentrallagern abgebildet.
Standorte:
1. Hamburg/Glinde
2. Augsburg
3. Erfurt
4. Lünen
5. Worms
- Implementierung Firmenfarmen / passend gestalten
- Passendes Icon die an den Standorten platziert sind.
(- Eventuell Umkeise in transparenter Farbe von 150KM um die einzelnen Standorte)

```html
<!DOCTYPE html>
<html lang="de">
<head>
<meta charset="utf-8">
<title>Standortübersicht – kabelkastenleihe.de</title>
<link rel="stylesheet" href="https://fonts.googleapis.com/css2?family=Raleway:wght@700&family=Roboto:wght@500;700&display=swap">
<style>
  :root {
    --paper: #ecebe6;
    --brand-blue: #1b4a82;
    --brand-orange: #d4731c;
    --map-blue: #1d4c85;
    --map-green: #6db33f;
    --pin-light: #ffffff;
  }
  html, body {
    margin: 0;
    padding: 0;
    width: 1200px;
    height: 800px;
    overflow: hidden;
    background: var(--paper);
  }
  .card {
    position: relative;
    width: 1200px;
    height: 800px;
    font-family: "Roboto", Arial, sans-serif;
  }
  .brand {
    position: absolute;
    left: 365px;
    top: 109px;
    display: flex;
    align-items: center;
    gap: 16px;
  }
  .brand-mark {
    width: 56px;
    height: 56px;
    background: var(--brand-blue);
  }
  .brand-name {
    font-family: "Raleway", Arial, sans-serif;
    font-weight: 700;
    font-size: 40px;
    color: var(--brand-blue);
    letter-spacing: 0.5px;
  }
  .germany-map {
    position: absolute;
    left: 400px;
    top: 300px;
    width: 430px;
    height: 330px;
    border-radius: 90px 120px 70px 110px;
    background: radial-gradient(ellipse at 45% 45%, var(--map-green) 0%, #4f8f4a 40%, var(--map-blue) 85%);
  }
  .connectors {
    position: absolute;
    inset: 0;
    pointer-events: none;
  }
  .connectors polyline {
    stroke: var(--brand-orange);
    stroke-width: 2;
    fill: none;
  }
  .connectors .leader-dot { fill: var(--brand-orange); }
  .connectors .site-pin { fill: var(--brand-orange); stroke: var(--pin-light); stroke-width: 2; }
  .connectors .site-pin-core { fill: var(--pin-light); }
  .location {
    position: absolute;
    line-height: 1;
  }
  .location--left { text-align: right; }
  .location--right { text-align: left; }
  .location-city {
    font-weight: 700;
    font-size: 23px;
    color: var(--brand-blue);
    margin-bottom: 9px;
  }
  .location-address {
    font-weight: 500;
    font-size: 16px;
    color: var(--brand-orange);
    line-height: 23px;
  }
  .headline {
    position: absolute;
    left: 906px;
    top: 556px;
    margin: 0;
    font-family: "Raleway", Arial, sans-serif;
    font-weight: 700;
    font-size: 48px;
    line-height: 58px;
    color: var(--brand-blue);
  }
</style>
</head>
<body>
<main class="card">
  <div class="brand">
    <div class="brand-mark"></div>
    <span class="brand-name">kabelkastenleihe.de</span>
  </div>

  <div class="germany-map" role="img" aria-label="Isometrische Deutschlandkarte mit Bundesländern in Blau und Grün und Verteilerkasten-Symbolen an den fünf Standorten"></div>

  <svg class="connectors" width="1200" height="800" viewBox="0 0 1200 800">
    <circle class="leader-dot" cx="307" cy="279" r="8"/>
    <polyline points="307,279 386,279 462,372"/>
    <circle class="leader-dot" cx="331" cy="404" r="8"/>
    <polyline points="331,404 411,404 482,492"/>
    <circle class="leader-dot" cx="370" cy="594" r="8"/>
    <polyline points="370,594 556,594 625,478"/>
    <circle class="leader-dot" cx="853" cy="248" r="8"/>
    <polyline points="853,248 773,248 712,348"/>
    <circle class="leader-dot" cx="906" cy="403" r="8"/>
    <polyline points="906,403 826,403 768,498"/>

    <g class="site-pins">
      <path class="site-pin" d="M462 372 c-9 -12 -14 -18 -14 -25 a14 14 0 0 1 28 0 c0 7 -5 13 -14 25z"/>
      <circle class="site-pin-core" cx="462" cy="347" r="5"/>
      <path class="site-pin" d="M482 492 c-9 -12 -14 -18 -14 -25 a14 14 0 0 1 28 0 c0 7 -5 13 -14 25z"/>
      <circle class="site-pin-core" cx="482" cy="467" r="5"/>
      <path class="site-pin" d="M625 478 c-9 -12 -14 -18 -14 -25 a14 14 0 0 1 28 0 c0 7 -5 13 -14 25z"/>
      <circle class="site-pin-core" cx="625" cy="453" r="5"/>
      <path class="site-pin" d="M712 348 c-9 -12 -14 -18 -14 -25 a14 14 0 0 1 28 0 c0 7 -5 13 -14 25z"/>
      <circle class="site-pin-core" cx="712" cy="323" r="5"/>
      <path class="site-pin" d="M768 498 c-9 -12 -14 -18 -14 -25 a14 14 0 0 1 28 0 c0 7 -5 13 -14 25z"/>
      <circle class="site-pin-core" cx="768" cy="473" r="5"/>
    </g>
  </svg>

  <div class="location location--left" style="right: 908px; top: 266px;">
    <div class="location-city">Hamburg</div>
    <div class="location-address">District Name Str. 18<br>78678 Lünen</div>
  </div>

  <div class="location location--left" style="right: 889px; top: 391px;">
    <div class="location-city">Lünen</div>
    <div class="location-address">District Name Str. 18<br>78678 Lünen</div>
  </div>

  <div class="location location--left" style="right: 851px; top: 581px;">
    <div class="location-city">Erfürt</div>
    <div class="location-address">District Name Str. 18<br>78678 Erfürt</div>
  </div>

  <div class="location location--right" style="left: 875px; top: 235px;">
    <div class="location-city">Worms</div>
    <div class="location-address">District Name Str. 18<br>78678 Worms</div>
  </div>

  <div class="location location--right" style="left: 928px; top: 390px;">
    <div class="location-city">Augsburg</div>
    <div class="location-address">District Name Str. 18<br>78678 Augsburg</div>
  </div>

  <h1 class="headline">Our Map<br>Locations</h1>
</main>
</body>
</html>
```